Consulting Company Business Card

I am looking for a minimalist, classy, professional design on my business card. I would like it to be double-sided. I want to use the font and color scheme of my logo which are attached. Please be creative in the designs that you send me. I want to play off the design of my logo with the inner C that is Green and Blue broken up with the white.
Target Market(s)
Small Businesses
Industry/Entity Type
Consulting
Contact Information for Business Card
Dale M. Whitcombe, CPA CGMA, 555-014-2873, dwhitcombe@vorantaadvisory.example, www.vorantaadvisory.example

```html
<!DOCTYPE html>
<html lang="en">
<head>
<meta charset="utf-8">
<title>Voranta Advisory – Business Card</title>
<link rel="stylesheet" href="https://fonts.googleapis.com/css2?family=Lexend:wght@300;400;500;600&display=swap">
<style>
  :root {
    --backdrop: #e4e4e2;
    --card: #fbfbfb;
    --navy: #2e3347;
    --teal: #2f8a84;
    --ink: #2b2b30;
    --shadow: rgba(40, 40, 45, 0.18);
  }
  * { box-sizing: border-box; margin: 0; padding: 0; }
  html, body {
    width: 1200px;
    height: 675px;
    overflow: hidden;
    background: var(--backdrop);
    font-family: "Lexend", "Helvetica Neue", Arial, sans-serif;
  }
  .sheet {
    width: 1200px;
    height: 675px;
    display: flex;
    align-items: center;
    justify-content: center;
    gap: 60px;
  }
  .card {
    position: relative;
    width: 500px;
    height: 286px;
    background: var(--card);
    border-radius: 16px;
    box-shadow: 0 10px 28px var(--shadow);
    overflow: hidden;
  }

  /* Shared company name block */
  .brand {
    text-align: center;
    color: var(--navy);
    font-weight: 600;
    letter-spacing: 0.06em;
    text-transform: uppercase;
    line-height: 1;
  }

  /* Contact side */
  .card--contact .brand {
    position: absolute;
    top: 78px;
    left: 0;
    right: 0;
    font-size: 26px;
  }
  .rule {
    position: absolute;
    left: 34px;
    right: 34px;
    top: 142px;
    height: 1.5px;
    background: var(--teal);
  }
  .contact-list {
    position: absolute;
    left: 34px;
    top: 158px;
    list-style: none;
    font-size: 12px;
    font-weight: 400;
    color: var(--ink);
  }
  .contact-list li {
    display: flex;
    align-items: center;
    gap: 8px;
    height: 22px;
    white-space: nowrap;
  }
  .contact-list svg {
    width: 12px;
    height: 12px;
    flex: none;
    fill: none;
    stroke: var(--teal);
    stroke-width: 1.6;
  }
  .person {
    position: absolute;
    right: 34px;
    top: 160px;
    text-align: right;
  }
  .person__name {
    font-size: 16px;
    font-weight: 500;
    letter-spacing: 0.05em;
    color: var(--ink);
    text-transform: uppercase;
    white-space: nowrap;
  }
  .person__credentials {
    width: 140px;
    margin: 12px 0 0 auto;
    padding-top: 5px;
    border-top: 1.5px solid var(--teal);
    font-size: 11px;
    letter-spacing: 0.08em;
    color: var(--teal);
  }

  /* Brand side */
  .card--brand {
    display: flex;
    align-items: center;
    justify-content: center;
  }
  .card--brand .brand {
    font-size: 34px;
  }
</style>
</head>
<body>
<main class="sheet">

  <section class="card card--contact" aria-label="Business card, contact side">
    <div class="brand">Voranta Advisory</div>
    <div class="rule"></div>

    <ul class="contact-list">
      <li>
        <svg viewBox="0 0 12 12" aria-hidden="true"><path d="M2.2 1.2h2l1 2.6-1.3.9a6 6 0 0 0 3.4 3.4l.9-1.3 2.6 1v2c0 .6-.5 1-1 1A9.2 9.2 0 0 1 1.2 2.2c0-.5.4-1 1-1z"/></svg>
        <span>555-014-2873</span>
      </li>
      <li>
        <svg viewBox="0 0 12 12" aria-hidden="true"><rect x="1" y="2.5" width="10" height="7" rx="1"/><path d="M1.3 3l4.7 3.6L10.7 3"/></svg>
        <span>dwhitcombe@vorantaadvisory.example</span>
      </li>
      <li>
        <svg viewBox="0 0 12 12" aria-hidden="true"><circle cx="6" cy="6" r="4.8"/><ellipse cx="6" cy="6" rx="2" ry="4.8"/><path d="M1.2 6h9.6"/></svg>
        <span>www.vorantaadvisory.example</span>
      </li>
    </ul>

    <div class="person">
      <div class="person__name">Dale M. Whitcombe</div>
      <div class="person__credentials">CPA CGM</div>
    </div>
  </section>

  <section class="card card--brand" aria-label="Business card, brand side">
    <div class="brand">Voranta Advisory</div>
  </section>

</main>
</body>
</html>
```